New Business Cards

We are a long time (57 years) independent pharmacy that needs a new look for a new generation. We are fast at what we do and don't have long lines to wait in. We are also more than a pharmacy as we carry lift chairs, walkers, ostomy supplies, wound care, nebulizers, and braces. I want to be able to use the look on facebook, twitter, postcards, letters, emails, and business cards. I want it to be something that when they see it they think Bluestone Corner Pharmacy.Our primary colors are red and blue. You can check out www.bluestonecornerpharmacy.net and www.friendwall.net/bluecornrx. We also are now a KPW contract holder.

The attached documents are some examples of things we like. and the jpg file is what we use now that does not work well for social media marketing or print marketing.

Target Market(s)

The primary audience we are looking at is going to be the 25 and older crowd.

Industry/Entity Type

Marketing

Font styles to use
Serif
Sans Serif

Colors
0255a3
ec2229

Requirements
Must have
• Name
Address
Facebook logo or address
contact info
Nice to have
• Twitter logo
KPW logo

```html
<!DOCTYPE html>
<html lang="en">
<head>
<meta charset="utf-8">
<title>Bluestone Corner Pharmacy – Business Card</title>
<link rel="stylesheet" href="https://fonts.googleapis.com/css2?family=Cinzel:wght@600&family=Open+Sans:wght@400;700&display=swap">
<style>
  :root {
    --brand-blue: #0255a3;
    --brand-red: #ec2229;
    --deep-blue: #0b3560;
    --mid-blue: #2f79b8;
    --light-blue: #6aa8da;
    --paper: #ffffff;
    --ink-blue: #1f4f8f;
    --canvas: #e9ecef;
  }
  * { box-sizing: border-box; margin: 0; padding: 0; }
  html, body {
    width: 1200px; height: 784px; overflow: hidden;
    background: var(--canvas);
  }
  .stage {
    position: relative; width: 1200px; height: 784px;
    display: flex; align-items: center; justify-content: center; gap: 40px;
  }
  .card {
    position: relative; width: 540px; height: 309px; overflow: hidden;
    box-shadow: 0 6px 18px rgba(0,0,0,.18);
  }

  /* Front */
  .card-front { background: var(--deep-blue); }
  .front-pattern {
    position: absolute; inset: 0;
    background:
      radial-gradient(ellipse at 85% 30%, var(--light-blue) 0%, transparent 55%),
      linear-gradient(120deg, var(--deep-blue) 0%, var(--mid-blue) 60%, var(--light-blue) 100%);
  }
  .front-brand {
    position: absolute; left: 0; right: 0; top: 96px;
    display: flex; flex-direction: column; align-items: center; gap: 14px;
  }
  .brand-dot {
    width: 52px; height: 52px; border-radius: 50%;
    background: var(--brand-red);
  }
  .front-name {
    font-family: "Cinzel", serif; font-weight: 600;
    font-size: 22px; letter-spacing: 1px; color: var(--paper);
  }

  /* Back */
  .card-back { background: var(--paper); }
  .back-brand {
    position: absolute; left: 26px; top: 30px;
    display: flex; align-items: center; gap: 14px;
  }
  .back-brand .brand-dot { width: 66px; height: 66px; }
  .back-name {
    font-family: "Cinzel", serif; font-weight: 600;
    font-size: 21px; color: var(--brand-blue); letter-spacing: .5px;
  }
  .person { position: absolute; left: 56px; top: 168px; }
  .person-name {
    font-family: "Open Sans", sans-serif; font-weight: 700;
    font-size: 17px; color: var(--brand-red);
  }
  .person-role {
    font-family: "Open Sans", sans-serif; font-size: 11px;
    color: var(--ink-blue);
  }
  .contact-list {
    position: absolute; left: 56px; top: 222px; list-style: none;
    font-family: "Open Sans", sans-serif; font-size: 11.5px; color: var(--ink-blue);
  }
  .contact-list li { display: flex; align-items: center; gap: 8px; height: 17px; }
  .contact-list svg { width: 13px; height: 13px; fill: var(--brand-red); flex: none; }

  .partner {
    position: absolute; right: 22px; top: 120px;
    display: flex; flex-direction: column; align-items: flex-end; gap: 6px;
  }
  .partner-badge {
    width: 46px; height: 36px; background: var(--brand-blue);
    display: flex; align-items: center; justify-content: center;
    font-family: "Open Sans", sans-serif; font-size: 12px; color: var(--paper);
  }
  .social-row { display: flex; gap: 4px; }
  .social-mark { width: 18px; height: 18px; background: var(--brand-blue); }
  .social-mark.alt { background: var(--light-blue); }
</style>
</head>
<body>
<main class="stage">

  <section class="card card-front">
    <div class="front-pattern" role="img" aria-label="Blue background with a sweeping pattern of soft light-blue circles"></div>
    <div class="front-brand">
      <span class="brand-dot"></span>
      <span class="front-name">Bluestone Corner Pharmacy</span>
    </div>
  </section>

  <section class="card card-back">
    <div class="back-brand">
      <span class="brand-dot"></span>
      <span class="back-name">Bluestone Corner Pharmacy</span>
    </div>

    <div class="partner">
      <div class="partner-badge">KPW</div>
      <div class="social-row">
        <span class="social-mark"></span>
        <span class="social-mark alt"></span>
      </div>
    </div>

    <div class="person">
      <p class="person-name">Nora Vance</p>
      <p class="person-role">Managing Director</p>
    </div>

    <ul class="contact-list">
      <li>
        <svg viewBox="0 0 16 16" aria-hidden="true"><path d="M8 1 1 7.5h2V15h4v-4h2v4h4V7.5h2z"/></svg>
        PO Box 41730 AL 35812
      </li>
      <li>
        <svg viewBox="0 0 16 16" aria-hidden="true"><path d="M3.5 1 6 4 4.5 6c1 2.2 3.3 4.5 5.5 5.5L12 10l3 2.5-1.5 2.5C7.5 15 1 8.5 1 2.5z"/></svg>
        1478 302 619
      </li>
      <li>
        <svg viewBox="0 0 16 16" aria-hidden="true"><path d="M1 3h14v10H1zm1.5 1.2V5l5.5 4 5.5-4v-.8z"/></svg>
        Nora@www.bluestonecornerpharmacy.net
      </li>
      <li>
        <svg viewBox="0 0 16 16" aria-hidden="true"><path d="M8 1a7 7 0 1 0 0 14A7 7 0 0 0 8 1zm0 1.5c.8 0 1.8 1.8 2 4.5H6c.2-2.7 1.2-4.5 2-4.5zM2.6 7a5.5 5.5 0 0 1 2.8-4C4.8 4 4.5 5.4 4.5 7zm0 2h1.9c0 1.6.3 3 .9 4a5.5 5.5 0 0 1-2.8-4zM6 9h4c-.2 2.7-1.2 4.5-2 4.5S6.2 11.7 6 9zm5.5 0h1.9a5.5 5.5 0 0 1-2.8 4c.6-1 .9-2.4.9-4zm0-2c0-1.6-.3-3-.9-4a5.5 5.5 0 0 1 2.8 4z"/></svg>
        www.eshop.bluestonecornerpharmacy.net
      </li>
    </ul>
  </section>

</main>
</body>
</html>
```